Financial Services Consultant needs a business card

We need a business card for a new consulting company based in Melbourne called
"Korvane Metrics". Tagline is Measure, Monitor, Save
We would like to see business card designs that are in line with the minimal style of the website www.korvane-metrics-example.com
The font I have used on the website is Proxima Nova and would like the same or similar font used on the business card with a minimal design in line with the website Two sided with "KORVANE METRICS" MEASURE, MONITOR, SAVE on one side and name, title and contact details on the otther
Updates

Hi All, thanks for your submissions, much appreciated.

I have recently added some colour to my webiste, it is hex #3a7b74 for those that wish to use it
Thanks

Hi all

thanks very much for your design submissions I am very impressed and they are much appreciated.

Interms of general feedback please find below;

Colour: I am trying to stick to a minimal design and colour scheme for my website which is still under construction, up to 3 colours( www.korvane-metrics-example.com) it is currently black and white with a small amount of blue/green but I am open to suggestion/interpretations for a consulting company.

Card: I dont mind if it has rounded edges or straight, I was thinking about using a letterpress card if possible

Detail: the detail on the card will include; Name, Title, Mobile, Personal Email, Business Email,Web,Business Address

Once again thanks for submissions

Industry/Entity Type

Business

```html
<!DOCTYPE html>
<html lang="en">
<head>
<meta charset="utf-8">
<title>Korvane Metrics — Business Card</title>
<link rel="stylesheet" href="https://fonts.googleapis.com/css2?family=Montserrat:wght@600;700&family=Exo+2:wght@300;400;500&display=swap">
<style>
  :root {
    --page: #e6e7e7;
    --card-light: #f7f7f7;
    --card-grey: #c9cbcb;
    --teal: #3a7b74;
    --teal-light: #5aaea1;
    --teal-mid: #3f8279;
    --teal-deep: #2f665f;
    --teal-dark: #25524c;
    --teal-ink: #1f4540;
    --white: #ffffff;
    --white-soft: rgba(255,255,255,.85);
  }
  * { margin: 0; padding: 0; box-sizing: border-box; }
  html, body { width: 1200px; height: 900px; overflow: hidden; background: var(--page); }
  .canvas { position: relative; width: 1200px; height: 900px; }

  .card {
    position: absolute; left: 320px; width: 560px; height: 320px;
    overflow: hidden;
    box-shadow: 0 10px 24px rgba(0,0,0,.22);
  }
  .card--front { top: 100px; }
  .card--back  { top: 480px; }
  .card-art { position: absolute; inset: 0; width: 100%; height: 100%; }

  /* front */
  .brand-name {
    position: absolute; left: 44px; top: 112px;
    font-family: "Montserrat", sans-serif; font-weight: 700;
    font-size: 38px; line-height: 46px; letter-spacing: .5px; color: var(--white); white-space: nowrap;
  }
  .brand-url {
    position: absolute; left: 46px; top: 162px;
    font-family: "Montserrat", sans-serif; font-weight: 700;
    font-size: 13.5px; line-height: 18px; letter-spacing: 2.6px; color: var(--white); white-space: nowrap;
  }
  .brand-tagline {
    position: absolute; left: 46px; top: 196px;
    font-family: "Exo 2", sans-serif; font-weight: 500;
    font-size: 13px; line-height: 16px; letter-spacing: 3.4px; color: var(--white-soft); white-space: nowrap;
  }

  /* back */
  .person-name {
    position: absolute; left: 20px; top: 116px; width: 212px; text-align: right;
    font-family: "Montserrat", sans-serif; font-weight: 700;
    font-size: 24px; line-height: 30px; color: var(--white); white-space: nowrap;
  }
  .person-title {
    position: absolute; left: 20px; top: 150px; width: 212px; text-align: right;
    font-family: "Exo 2", sans-serif; font-weight: 400;
    font-size: 13px; line-height: 16px; letter-spacing: .6px; color: var(--white); white-space: nowrap;
  }
  .contact-item {
    position: absolute; left: 350px;
    font-family: "Exo 2", sans-serif; font-weight: 300;
    font-size: 13px; line-height: 16px; color: var(--white); white-space: nowrap;
  }
  .contact-item--address { top: 80px; }
  .contact-item--phone { top: 129px; }
  .contact-item--mail { top: 174px; }
  .contact-item--web { top: 219px; font-weight: 400; }
  .back-brand {
    position: absolute; left: 350px; top: 270px;
    font-family: "Montserrat", sans-serif; font-weight: 700;
    font-size: 16px; line-height: 20px; color: var(--teal-ink); white-space: nowrap;
  }
</style>
</head>
<body>
<main class="canvas">

  <section class="card card--front" aria-label="Business card front">
    <svg class="card-art" viewBox="0 0 560 320" aria-hidden="true">
      <defs>
        <linearGradient id="frontPaper" x1="0" y1="0" x2="1" y2="1">
          <stop offset="0" stop-color="var(--card-light)"/>
          <stop offset="1" stop-color="var(--card-grey)"/>
        </linearGradient>
        <linearGradient id="frontBand" x1="0" y1="0" x2="1" y2="1">
          <stop offset="0" stop-color="var(--teal-mid)"/>
          <stop offset="1" stop-color="var(--teal-deep)"/>
        </linearGradient>
      </defs>
      <rect width="560" height="320" fill="url(#frontPaper)"/>
      <polygon points="420,0 560,0 560,320 470,320" fill="#dcdede"/>
      <polygon points="0,62 440,62 486,258 0,258" fill="url(#frontBand)"/>
    </svg>
    <p class="brand-name">KORVANE METRICS</p>
    <p class="brand-url">WWW.KORVANE-METRICS-EXAMPLE.COM</p>
    <p class="brand-tagline">MEASURE, MONITOR, SAVE</p>
  </section>

  <section class="card card--back" aria-label="Business card back">
    <svg class="card-art" viewBox="0 0 560 320" aria-hidden="true">
      <defs>
        <linearGradient id="backPaper" x1="0" y1="0" x2="1" y2="1">
          <stop offset="0" stop-color="var(--white)"/>
          <stop offset="1" stop-color="#d6d8d8"/>
        </linearGradient>
      </defs>
      <rect width="560" height="320" fill="url(#backPaper)"/>
      <polygon points="0,40 232,40 262,268 0,268" fill="var(--teal-mid)"/>
      <polygon points="268,30 300,30 322,300 292,300" fill="#e3e5e5"/>
      <rect x="300" y="62" width="36" height="52" fill="var(--teal-light)"/>
      <rect x="300" y="114" width="36" height="46" fill="var(--teal-mid)"/>
      <rect x="300" y="160" width="36" height="45" fill="var(--teal-deep)"/>
      <rect x="300" y="205" width="36" height="45" fill="var(--teal-dark)"/>
      <rect x="336" y="62" width="224" height="52" fill="#4f9c90"/>
      <rect x="336" y="114" width="224" height="46" fill="#3a7b74"/>
      <rect x="336" y="160" width="224" height="45" fill="#316b64"/>
      <rect x="336" y="205" width="224" height="45" fill="#295a54"/>
      <rect x="336" y="250" width="224" height="6" fill="var(--teal-ink)"/>
      <g fill="var(--white)">
        <path d="M318 78a7 7 0 0 0-7 7c0 5 7 12 7 12s7-7 7-12a7 7 0 0 0-7-7zm0 10a3 3 0 1 1 0-6 3 3 0 0 1 0 6z"/>
        <path d="M313 128h10a1.5 1.5 0 0 1 1.5 1.5v15a1.5 1.5 0 0 1-1.5 1.5h-10a1.5 1.5 0 0 1-1.5-1.5v-15a1.5 1.5 0 0 1 1.5-1.5zm.5 2.5v11.5h9v-11.5z"/>
        <path d="M310 177h16v11h-16zm1.5 1.5l6.5 5 6.5-5z" fill-rule="evenodd"/>
        <path d="M313 220l12 6-5 1.5 3 5-2 1-3-5-4 3z"/>
      </g>
    </svg>
    <p class="person-name">YOUR NAME</p>
    <p class="person-title">YOUR DESIGNATION</p>
    <p class="contact-item contact-item--address">Your Address, Your City, 1234<br>Lorem ipsum dolor sit amet</p>
    <p class="contact-item contact-item--phone">+012 345 67 89</p>
    <p class="contact-item contact-item--mail">mail@website.com</p>
    <p class="contact-item contact-item--web">www.website.com</p>
    <p class="back-brand">KORVANE METRICS</p>
  </section>

</main>
</body>
</html>
```